Marlow Realty Real Estate Brokerage Recruiting Flyer

We are a real estate brokerage looking to hire more real estate agents. We need to list everything we have to offer as a company so real estate agents will join our company. this is our company website: www.Marlowrealty.example .

100% COMMISSION NO MONTHLY FEE
$450 Flat Transaction FEE

What We Offer:
24/7 Office Access
Free E & O Insurance for 1st Year
Free Online CE and PLE
Free 1,000 Business Cards
Free Professional Social Media Marketing
Free Printing, Scanning, and Copies
Free Buyer and Seller Presentation Packages
Free Filquay Cloud Based Document Management Access
Access to our Internal Brokerage Forum
Company Profit Sharing!
Private Offices Available to Rent

*Lead Generation Software with over 3,000 Leads
*10 Leads to Start
* Free Personal CRM and Website
*Restrictions and Rules apply

Company Address:
4817 Amberfield Road
Suite 512
Fairfax, VA 22194
Phone: 703-555-0147
email: info@marlowrealty.example

Target Market(s)

Real Estate Agents

Industry/Entity Type

Real Estate

Colors
0555a3
ffffff

Requirements
Must have
• 100% COMMISSION NO MONTHLY FEE
$450 Flat Transaction FEE

What We Offer:
24/7 Office Access
Free Online CE and PLE
Free 1,000 Business Cards
Company Profit Sharing!

*10 Leads to Start

Company Address:
4817 Amberfield Road
Suite 512
Fairfax, VA 22194
Phone: 703-555-0147

```html
<!DOCTYPE html>
<html lang="en">
<head>
<meta charset="utf-8">
<title>Marlow Realty – Agent Recruiting Flyer</title>
<link rel="stylesheet" href="https://fonts.googleapis.com/css2?family=Montserrat:wght@600;700;800&family=Open+Sans:ital,wght@0,400;0,600;0,700;1,400&display=swap">
<style>
  :root {
    --brand-blue: #0555a3;
    --accent-green: #1fb51f;
    --ink: #111111;
    --paper: #ffffff;
    --mist-top: #f4f4f5;
    --mist-bottom: #c9cacd;
    --stage: #e9eef2;
  }
  * { box-sizing: border-box; margin: 0; padding: 0; }
  html, body { width: 1200px; height: 810px; overflow: hidden; background: var(--stage); }
  .flyer {
    position: absolute; left: 300px; top: 17px; width: 600px; height: 776px;
    background: linear-gradient(160deg, var(--mist-top) 0%, var(--mist-bottom) 55%);
    overflow: hidden; font-family: "Open Sans", Arial, sans-serif; color: var(--ink);
    box-shadow: 0 6px 24px rgba(0,0,0,.18);
  }
  .agent-photo {
    position: absolute; left: 40px; top: 165px; width: 230px; height: 290px;
    background: linear-gradient(180deg, #b58d74 0%, #b58d74 28%, #2a2d33 30%, #1b1d22 100%);
    border-radius: 40% 40% 0 0;
  }
  .wave { position: absolute; left: 0; top: 0; width: 600px; height: 776px; }
  .house-photo {
    position: absolute; left: 240px; top: 228px; width: 124px; height: 124px; border-radius: 50%;
    background: linear-gradient(180deg, #5b6d86 0%, #cdb998 55%, #8d9a72 100%);
    border: 4px solid var(--brand-blue);
  }
  .headline {
    position: absolute; right: 40px; top: 32px; text-align: right;
    font-family: "Montserrat", Arial, sans-serif; font-weight: 800; font-size: 30px; line-height: 1.05;
  }
  .headline .blue { color: var(--brand-blue); }
  .offer-terms { position: absolute; right: 40px; top: 150px; text-align: right; font-family: "Montserrat", Arial, sans-serif; }
  .offer-terms .commission { font-weight: 700; font-size: 13px; }
  .offer-terms .commission .pct { color: var(--accent-green); }
  .offer-terms .flat-fee { font-weight: 800; font-size: 20px; color: var(--brand-blue); }
  .section-title {
    font-family: "Montserrat", Arial, sans-serif; font-weight: 800; color: var(--brand-blue); font-size: 16px; line-height: 20px;
  }
  .benefits { position: absolute; left: 318px; top: 300px; width: 270px; }
  .benefits .section-title { margin-left: 40px; margin-bottom: 28px; }
  .benefit-list { list-style: none; font-size: 12.5px; line-height: 18px; }
  .benefit-list li { position: relative; padding-left: 22px; }
  .benefit-list li svg { position: absolute; left: 0; top: 4px; width: 14px; height: 11px; }
  .lead-notes { position: absolute; left: 350px; top: 600px; width: 240px; font-size: 12.5px; line-height: 17px; }
  .lead-notes .highlight { color: var(--brand-blue); margin-bottom: 6px; }
  .lead-notes .perk { font-weight: 700; }
  .about { position: absolute; left: 30px; top: 466px; width: 280px; }
  .about p { font-style: italic; font-size: 13px; line-height: 17.5px; margin-top: 6px; }
  .brand { position: absolute; left: 40px; top: 594px; display: flex; align-items: center; gap: 10px; }
  .brand-square { width: 28px; height: 28px; background: var(--brand-blue); }
  .brand-name { font-family: "Montserrat", Arial, sans-serif; font-weight: 700; font-size: 24px; line-height: 28px; color: var(--brand-blue); }
  .contact { position: absolute; left: 40px; top: 636px; font-size: 12.5px; font-weight: 700; line-height: 16px; font-style: normal; }
  .contact .section-title { margin-bottom: 2px; }
  .licensing {
    position: absolute; right: 30px; top: 702px; font-family: "Montserrat", Arial, sans-serif;
    font-weight: 800; font-size: 15px; line-height: 20px; color: var(--brand-blue);
  }
</style>
</head>
<body>
<main class="flyer">
  <div class="agent-photo" role="img" aria-label="Photo of a smiling real estate agent in a dark suit with arms crossed"></div>

  <svg class="wave" viewBox="0 0 600 776" aria-hidden="true">
    <path d="M0,440 C150,335 330,255 600,238 L600,776 L0,776 Z" fill="var(--paper)"/>
    <path d="M0,440 C150,335 330,255 600,238" fill="none" stroke="var(--brand-blue)" stroke-width="10"/>
  </svg>

  <div class="house-photo" role="img" aria-label="Photo of a two-storey suburban house with a garage"></div>

  <h1 class="headline">THE BEST<br><span class="blue">BUSINESS ARE</span><br>AVAILABLE HERE</h1>

  <div class="offer-terms">
    <p class="commission"><span class="pct">100%</span> COMMISSION NO MONTHLY FEE</p>
    <p class="flat-fee">$450 Flat Transaction FEE</p>
  </div>

  <section class="benefits">
    <h2 class="section-title">WHAT WE OFFER</h2>
    <ul class="benefit-list">
      <li><svg viewBox="0 0 14 11"><path d="M0,0 L14,5.5 L0,11 L4,5.5 Z" fill="var(--brand-blue)"/></svg>24/7 Office Access</li>
      <li><svg viewBox="0 0 14 11"><path d="M0,0 L14,5.5 L0,11 L4,5.5 Z" fill="var(--brand-blue)"/></svg>Free E &amp; O Insurance for 1st Year</li>
      <li><svg viewBox="0 0 14 11"><path d="M0,0 L14,5.5 L0,11 L4,5.5 Z" fill="var(--brand-blue)"/></svg>Free Online CE and PLE</li>
      <li><svg viewBox="0 0 14 11"><path d="M0,0 L14,5.5 L0,11 L4,5.5 Z" fill="var(--brand-blue)"/></svg>Free 1,000 Business Cards</li>
      <li><svg viewBox="0 0 14 11"><path d="M0,0 L14,5.5 L0,11 L4,5.5 Z" fill="var(--brand-blue)"/></svg>Free Professional Social Media Marketing</li>
      <li><svg viewBox="0 0 14 11"><path d="M0,0 L14,5.5 L0,11 L4,5.5 Z" fill="var(--brand-blue)"/></svg>Free Printing, Scanning, and Copies</li>
      <li><svg viewBox="0 0 14 11"><path d="M0,0 L14,5.5 L0,11 L4,5.5 Z" fill="var(--brand-blue)"/></svg>Free Buyer and Seller Presentation Packages</li>
      <li><svg viewBox="0 0 14 11"><path d="M0,0 L14,5.5 L0,11 L4,5.5 Z" fill="var(--brand-blue)"/></svg>Access to our Internal Brokerage Forum</li>
      <li><svg viewBox="0 0 14 11"><path d="M0,0 L14,5.5 L0,11 L4,5.5 Z" fill="var(--brand-blue)"/></svg>Company Profit Sharing!</li>
      <li><svg viewBox="0 0 14 11"><path d="M0,0 L14,5.5 L0,11 L4,5.5 Z" fill="var(--brand-blue)"/></svg>Private Offices Available to Rent</li>
      <li><svg viewBox="0 0 14 11"><path d="M0,0 L14,5.5 L0,11 L4,5.5 Z" fill="var(--brand-blue)"/></svg>Free Filquay Cloud Based Document Management Access</li>
    </ul>
  </section>

  <section class="lead-notes">
    <p class="highlight">*Lead Generation Software with over 3,000 Leads</p>
    <p class="perk">*10 Leads to Start</p>
    <p class="perk">* Free Personal CRM and Website</p>
    <p class="perk">*Restrictions and Rules apply</p>
  </section>

  <section class="about">
    <h2 class="section-title">ABOUT US....</h2>
    <p>We are a real estate brokerage looking to hire more real estate agents. We need to list everything we have to offer as a company so real estate agents will join our company.</p>
  </section>

  <div class="brand">
    <span class="brand-square"></span>
    <span class="brand-name">Marlow Realty</span>
  </div>

  <address class="contact">
    <h2 class="section-title">Company Address:</h2>
    4817 Amberfield Road<br>
    Suite 512<br>
    Fairfax, VA 22194<br>
    Phone: 703-555-0147<br>
    email: info@marlowrealty.example<br>
    www.Marlowrealty.example
  </address>

  <p class="licensing">Licensed in D.C., Maryland, and Virginia</p>
</main>
</body>
</html>
```